KORVAL Student Exchange needs a brochure design

I need a brochure design for KORVAL Student Exchange based in Auckland, New Zealand. I am responsible for outbound exchanges where I recruit local students from around New Zealand between the ages of 15 and 18 who are interested in going on an exchange overseas. Students can select from 12 different countries including America, France, Italy, the Netherlands, Spain, Ireland, Germany, Brazil Japan, and Argentina and choose the programme length from 3 months to an academic year (although we offer shorter programmes for some countries). I would like to attract students who are keen to learn about other cultures and experience something completely different to home. I would like to see vibrant colours and images that coveys fun, youthfulness and adventure.
Updates

Hi,

I have added pics and content for your viewing. 

Thanks.

Tessa

Hi,

Could I request that the designs are done on a tri-fold brochure

Also, I would like to see vibrant colours. So far, I have seen colours matching the logo (which is ok)  but I want to try and move away from that and start something fresh. Please look at the booklet and fee sheet which I have uploaded for ideas. 

I am wondering whether there is too much writing to fit on a tri fold brochure...
If you are having problems fitting everything in, please let me know.

I think the testimonial section could use up 2 spaces on the brochure. 

Target Market(s)

I would like to target teenagers who are interested in other cultures and want to enhance their language learning

Industry/Entity Type

Learn

Font styles to use
Serif
Sans Serif
Decorative

```html
<!DOCTYPE html>
<html lang="en">
<head>
<meta charset="utf-8">
<title>KORVAL Student Exchange – Tri-fold Brochure, Outside</title>
<link rel="stylesheet" href="https://fonts.googleapis.com/css2?family=Oswald:wght@400;500;600;700&family=Arimo:wght@400;700&display=swap">
<style>
  :root{
    --stage:#5d5d5d;
    --navy:#0f2a6b;
    --navy-deep:#0a1c4a;
    --yellow:#ffd21f;
    --teal-top:#8fd8e6;
    --teal-bottom:#d8f3f6;
    --white:#ffffff;
    --ink:#1d2333;
    --step-1:#ffd21f;
    --step-2:#19b3e6;
    --step-3:#f58a1f;
    --step-4:#ffe04d;
    --step-5:#8a4fc7;
    --step-6:#6f8fb8;
    --photo-sky:#9fc3e0;
    --photo-stone:#b89a7a;
    --photo-green:#6e8f5a;
  }
  *{box-sizing:border-box;margin:0;padding:0}
  html,body{width:770px;height:1200px;overflow:hidden}
  body{background:var(--stage);font-family:"Arimo",Arial,sans-serif;color:var(--ink);position:relative}

  .brochure{position:absolute;left:25px;top:370px;width:720px;height:460px;display:flex;box-shadow:0 6px 18px rgba(0,0,0,.35)}
  .panel{position:relative;width:240px;height:460px;overflow:hidden;background:var(--white)}

  /* Inside flap (left) */
  .group-photo{position:absolute;inset:0 0 118px 0;background:linear-gradient(180deg,var(--photo-sky) 0%,#d9c4a4 45%,var(--photo-stone) 70%,#4f5f7a 100%)}
  .group-photo__shade{position:absolute;left:0;right:0;top:190px;height:152px;background:linear-gradient(180deg,rgba(10,28,74,0) 0%,rgba(10,28,74,.75) 35%,rgba(10,28,74,.92) 100%)}
  .spine-title{position:absolute;left:4px;top:338px;transform-origin:left top;transform:rotate(-90deg);font-family:"Oswald",sans-serif;font-weight:700;font-size:24px;color:var(--white);letter-spacing:.5px;white-space:nowrap}
  .highlights{position:absolute;left:40px;right:8px;top:228px;list-style:none;color:var(--white);font-family:"Oswald",sans-serif;font-weight:400;font-size:12.6px;line-height:1.28}
  .on-your-side{position:absolute;left:0;right:0;bottom:0;height:118px;background:var(--yellow)}
  .on-your-side__title{position:absolute;left:52px;top:8px;font-family:"Oswald",sans-serif;font-weight:700;font-size:14px;color:var(--navy)}
  .student-photo{position:absolute;left:8px;top:30px;width:62px;height:80px;border-radius:30px 30px 4px 4px;background:linear-gradient(180deg,#e8b98e,#6b4a36 60%,#c68b3b)}
  .on-your-side__text{position:absolute;left:78px;right:8px;top:30px;font-size:9px;line-height:1.3;color:var(--navy-deep)}
  .on-your-side__text p+p{margin-top:5px}

  /* Back cover (middle) */
  .steps-area{position:absolute;inset:0 0 170px 0;background:linear-gradient(180deg,var(--teal-top),var(--teal-bottom))}
  .steps-title{margin-top:12px;text-align:center;font-family:"Oswald",sans-serif;font-weight:700;font-size:19px;color:var(--navy)}
  .steps-subtitle{text-align:center;font-size:8px;font-weight:700;color:var(--navy);margin-top:1px}
  .steps{list-style:none;margin:8px 8px 0}
  .step{display:flex;gap:6px;align-items:flex-start;min-height:37px;margin-bottom:2px}
  .step__label{flex:0 0 76px;height:13px;padding:0 4px;font-size:6.4px;font-weight:700;line-height:13px;color:var(--ink);white-space:nowrap}
  .step__label--1{background:var(--step-1)}
  .step__label--2{background:var(--step-2);color:var(--white)}
  .step__label--3{background:var(--step-3);color:var(--white)}
  .step__label--4{background:var(--step-4)}
  .step__label--5{background:var(--step-5);color:var(--white)}
  .step__label--6{background:var(--step-6);color:var(--white)}
  .step__text{font-size:6.4px;line-height:1.3;color:var(--ink)}
  .contact{position:absolute;left:0;right:0;bottom:0;height:170px;padding:8px 14px}
  .contact__lead{text-align:center;font-size:7.5px;font-style:italic;color:var(--ink)}
  .brand{display:flex;align-items:center;gap:6px;margin-top:6px}
  .brand__dot{width:20px;height:20px;border-radius:50%;background:var(--navy);flex:0 0 20px}
  .brand__name{font-family:"Oswald",sans-serif;font-weight:600;font-size:17px;color:var(--navy);line-height:1}
  .brand__full{font-size:7px;color:var(--navy);margin:2px 0 6px 26px}
  .contact__list{list-style:none;font-size:8.5px;line-height:1.25}
  .contact__list li{display:flex;align-items:center;gap:6px;margin-bottom:4px}
  .contact__list svg{flex:0 0 11px;width:11px;height:11px}
  .contact__label{display:block;font-size:6.5px;color:#555;margin-bottom:1px}
  .contact__web{font-weight:700;font-size:10px}

  /* Front cover (right) */
  .castle-photo{position:absolute;inset:0 0 160px 0;background:linear-gradient(180deg,#b9d6ec 0%,#cfdbe4 35%,#a7998c 62%,var(--photo-green) 85%,#3f4b3a 100%)}
  .cover-band{position:absolute;left:0;right:0;top:300px;height:30px;background:var(--yellow);font-family:"Oswald",sans-serif;font-weight:700;font-size:22px;line-height:30px;text-align:center;color:var(--navy)}
  .cover-tagline{position:absolute;left:0;right:0;top:330px;height:52px;background:var(--navy);padding:4px 14px;font-family:"Oswald",sans-serif;font-weight:500;font-size:18px;line-height:22px;color:var(--white)}
  .cover-brand{position:absolute;left:0;right:0;top:382px;bottom:0;padding:12px 30px 0}
  .cover-brand .brand{margin-top:0}
  .cover-brand .brand__name{font-size:19px}
  .cover-brand__note{font-size:9px;font-weight:700;color:var(--navy);margin:4px 0 0 26px}
</style>
</head>
<body>
<main class="brochure" aria-label="KORVAL Student Exchange tri-fold brochure, outside">

  <section class="panel panel--flap">
    <div class="group-photo" role="img" aria-label="Photo of a cheerful group of exchange students waving in a European town square"></div>
    <div class="group-photo__shade"></div>
    <h2 class="spine-title">STUDENT EXCHANGE</h2>
    <ul class="highlights">
      <li>Have the adventure of a lifetime</li>
      <li>Immerse yourself in a new culture</li>
      <li>Sharpen those language skills</li>
      <li>Make awesome new friends</li>
      <li>You'll gain confidence and a sense of independence that will probably exceed your expectations!</li>
    </ul>
    <div class="on-your-side">
      <h3 class="on-your-side__title">WE ARE ON YOUR SIDE</h3>
      <div class="student-photo" role="img" aria-label="Photo of a smiling student holding a pretzel"></div>
      <div class="on-your-side__text">
        <p>You are not just another client to us, not just another number. You choose the country and programme.</p>
        <p>We'll take care of the rest and as a non-profit organization, you can count on us to keep costs to a minimum.</p>
      </div>
    </div>
  </section>

  <section class="panel panel--back">
    <div class="steps-area">
      <h2 class="steps-title">HOW TO GET STARTED</h2>
      <p class="steps-subtitle">After you have chosen your destination and programme</p>
      <ol class="steps">
        <li class="step"><span class="step__label step__label--1">Step 1. INITIAL APPLICATION</span><span class="step__text">Complete the initial application form and post it to us with a $50 deposit (downloadable from our website).</span></li>
        <li class="step"><span class="step__label step__label--2">Step 2. FULL APPLICATION</span><span class="step__text">We will get in touch with you and send you the full application form.</span></li>
        <li class="step"><span class="step__label step__label--3">Step 3. INTERVIEW</span><span class="step__text">Once you have submitted your full application form to us, we will arrange an interview with you and either both or one of your parents.</span></li>
        <li class="step"><span class="step__label step__label--4">Step 4. ACCEPTANCE</span><span class="step__text">Once you are accepted, we will start arranging your flights, insurance, visa, host family and school placement.</span></li>
        <li class="step"><span class="step__label step__label--5">Step 5. ORIENTATION</span><span class="step__text">You will have an orientation about a month prior to departure to prepare you for your exchange. (You will also have one in your host country.)</span></li>
        <li class="step"><span class="step__label step__label--6">Step 6. BON VOYAGE</span><span class="step__text">Have your adventure begin! A KORVAL representative will see you off at the airport, and the host organisation will meet you and help you settle with your host family.</span></li>
      </ol>
    </div>
    <div class="contact">
      <p class="contact__lead">For more information on our exchange programmes, visit</p>
      <div class="brand"><span class="brand__dot"></span><span class="brand__name">KORVAL Student Exchange</span></div>
      <p class="brand__full">Korval Institute for Intercultural Learning</p>
      <ul class="contact__list">
        <li><svg viewBox="0 0 12 12"><circle cx="6" cy="6" r="5" fill="none" stroke="#0f2a6b" stroke-width="1.2"/><path d="M1 6h10M6 1c-2.5 3-2.5 7 0 10M6 1c2.5 3 2.5 7 0 10" fill="none" stroke="#0f2a6b" stroke-width=".9"/></svg><span><span class="contact__label">Official Website</span><span class="contact__web">www.korval-exchange.co.nz</span></span></li>
        <li><svg viewBox="0 0 12 12"><rect x="1" y="1" width="10" height="10" rx="2" fill="#0f2a6b"/></svg><span>social.korval-exchange.co.nz</span></li>
        <li><svg viewBox="0 0 12 12"><path d="M6 11C3 7.5 2 6 2 4.5a4 4 0 0 1 8 0C10 6 9 7.5 6 11z" fill="#0f2a6b"/><circle cx="6" cy="4.5" r="1.5" fill="#fff"/></svg><span>14 Harbour Lane/PO Box 40117<br>Ellerslie, Auckland, New Zealand 1051</span></li>
        <li><svg viewBox="0 0 12 12"><path d="M3 1l2 2.5-1.2 1.5c.7 1.4 1.8 2.5 3.2 3.2L8.5 7 11 9l-1.5 2C5 10.5 1.5 7 1 2.5z" fill="#0f2a6b"/></svg><span>09-555 0142, 0800 555 019</span></li>
        <li><svg viewBox="0 0 12 12"><rect x="1" y="2.5" width="10" height="7" rx="1" fill="none" stroke="#0f2a6b" stroke-width="1.2"/><path d="M1.5 3l4.5 3.5L10.5 3" fill="none" stroke="#0f2a6b" stroke-width="1.1"/></svg><span>tessa@korval.co.nz</span></li>
      </ul>
    </div>
  </section>

  <section class="panel panel--front">
    <div class="castle-photo" role="img" aria-label="Photo of two students posing in front of a fairytale castle"></div>
    <h1 class="cover-band">STUDENT EXCHANGE</h1>
    <p class="cover-tagline">The time of your life;<br>An experience for life</p>
    <div class="cover-brand">
      <div class="brand"><span class="brand__dot"></span><span class="brand__name">KORVAL Student Exchange</span></div>
      <p class="brand__full">Korval Institute for Intercultural Learning</p>
      <p class="cover-brand__note">non-profit, charitable organisation</p>
    </div>
  </section>

</main>
</body>
</html>
```